Postcard Design

The company is a global consulting company that is focusing on start-up business solutions and trade show management in the USA and overseas. The company web site is www.veltrapro.com.

We need the postcard to inform previous clients and industry contacts about our company.

We would like to see a design that includes the main colors of the logo, as well as the global consulting aspect.

The logo is attached.
Updates

Target Market(s)

Start-up business and trade shows element

Industry/Entity Type

Business

Requirements
Must have
• The logo needs to be included,

The international and start-up business ideas should be implemented.

```html
<!DOCTYPE html>
<html lang="en">
<head>
<meta charset="utf-8">
<title>Veltra Pro Postcard</title>
<link rel="stylesheet" href="https://fonts.googleapis.com/css2?family=Open+Sans:wght@400;600;700;800&display=swap">
<style>
  :root {
    --page: #e7e4df;
    --ink: #3d3d40;
    --muted: #6a6a6e;
    --bar: #4a4a4d;
    --bar-dark: #3a3a3c;
    --blue: #3f7fd0;
    --blue-soft: rgba(74, 132, 210, 0.88);
    --white: #ffffff;
    --mail-side: #f1f1f2;
  }
  * { margin: 0; padding: 0; box-sizing: border-box; }
  html, body { width: 1200px; height: 1000px; overflow: hidden; }
  body {
    background: var(--page);
    font-family: "Open Sans", Arial, sans-serif;
    color: var(--ink);
    position: relative;
  }
  .postcard {
    position: absolute;
    left: 210px;
    width: 780px;
    height: 470px;
    background: var(--white);
    overflow: hidden;
    box-shadow: 0 4px 14px rgba(0,0,0,0.18);
  }
  .postcard--back { top: 20px; }
  .postcard--front { top: 510px; }

  /* Back side */
  .design-column { position: absolute; left: 0; top: 0; width: 400px; height: 470px; }
  .mail-side {
    position: absolute; left: 400px; top: 0; width: 380px; height: 470px;
    background: linear-gradient(180deg, #f7f7f8, var(--mail-side));
  }
  .team-photo {
    position: absolute; left: 0; top: 0; width: 400px; height: 200px;
    background: linear-gradient(120deg, #2d3440 0%, #5a6270 40%, #cfd3da 70%, #eef0f3 100%);
  }
  .tagline {
    position: absolute; left: 22px; bottom: 18px;
    color: var(--white); font-weight: 800; font-size: 27px; line-height: 1.05;
    letter-spacing: 1px; text-transform: uppercase;
  }
  .services { position: absolute; left: 0; top: 200px; width: 400px; height: 190px; padding: 16px 22px; }
  .services-title { color: var(--blue); font-weight: 800; font-size: 13px; letter-spacing: 0.5px; margin-bottom: 6px; }
  .services-lists { display: flex; gap: 30px; }
  .services-lists ul { list-style: none; font-size: 11px; line-height: 1.5; color: var(--muted); }
  .services-lists li::before { content: "• "; color: var(--blue); }
  .services-note { font-size: 10px; color: var(--muted); margin-top: 6px; }
  .back-footer {
    position: absolute; left: 0; top: 390px; width: 400px; height: 80px;
    background: var(--bar); display: flex; align-items: center; padding: 0 18px; gap: 16px;
  }
  .logo-box {
    background: var(--white); display: flex; align-items: center; gap: 6px;
    padding: 8px 10px; font-weight: 700; font-size: 14px; color: var(--blue);
  }
  .logo-box .mark { width: 12px; height: 12px; background: var(--blue); }
  .contact-list { list-style: none; color: var(--white); font-size: 11.5px; font-weight: 600; line-height: 1.55; }
  .contact-list li { display: flex; align-items: center; gap: 6px; }
  .contact-list svg, .front-footer svg { width: 12px; height: 12px; fill: var(--white); flex: none; }

  /* Front side */
  .hero-photo {
    position: absolute; left: 0; top: 0; width: 780px; height: 300px;
    background: linear-gradient(100deg, #b9c1cc 0%, #dfe3e8 35%, #f4f5f7 60%, #d7dce3 100%);
  }
  .headline {
    position: absolute; left: 28px; top: 36px;
    color: var(--white); font-weight: 800; font-size: 34px; line-height: 1.08;
    text-transform: uppercase; letter-spacing: 1px;
    text-shadow: 0 1px 3px rgba(0,0,0,0.2);
  }
  .intro-box {
    position: absolute; left: 300px; top: 176px; width: 480px; height: 94px;
    background: var(--blue-soft); color: var(--white);
    font-size: 11.5px; line-height: 1.5; padding: 12px 18px;
  }
  .front-logo {
    position: absolute; left: 28px; top: 232px; height: 56px;
    padding: 0 18px; font-size: 18px;
  }
  .about { position: absolute; left: 0; top: 300px; width: 780px; height: 122px; padding: 12px 28px; }
  .about h2 { color: var(--blue); font-size: 13px; font-weight: 800; margin-bottom: 2px; }
  .about p { font-size: 10.5px; line-height: 1.45; color: var(--muted); margin-bottom: 6px; }
  .front-footer {
    position: absolute; left: 0; top: 422px; width: 780px; height: 48px;
    background: var(--bar); color: var(--white);
    display: flex; align-items: center; justify-content: space-between; padding: 0 28px;
    font-size: 13px; font-weight: 700;
  }
  .front-footer span { display: flex; align-items: center; gap: 7px; }
</style>
</head>
<body>

<section class="postcard postcard--back">
  <div class="design-column">
    <div class="team-photo" role="img" aria-label="Photo of a business team working together at a laptop"></div>
    <p class="tagline">Connected.<br>Informed.<br>Focused</p>
    <div class="services">
      <h3 class="services-title">GLOBAL SERVICE PACKAGES</h3>
      <div class="services-lists">
        <ul>
          <li>Accounting*</li><li>Coaching</li><li>Event Planning*</li><li>IT Support*</li>
          <li>Location Finder</li><li>Market Research</li><li>Product Introduction</li>
          <li>Staff/Recruiting</li><li>Vendor Selection</li>
        </ul>
        <ul>
          <li>Business Evaluation</li><li>Cross Cultural Training</li><li>Global Telemarketing</li>
          <li>Legal Support*</li><li>Marketing</li><li>Office Management*</li>
          <li>Product Sourcing</li><li>Trade Show Planning</li>
        </ul>
      </div>
      <p class="services-note">* Through third party contact and providers</p>
    </div>
    <div class="back-footer">
      <div class="logo-box"><span class="mark"></span>Veltra Pro</div>
      <ul class="contact-list">
        <li><svg viewBox="0 0 24 24"><path d="M6.6 10.8a15 15 0 0 0 6.6 6.6l2.2-2.2a1 1 0 0 1 1-.25 11.4 11.4 0 0 0 3.6.57 1 1 0 0 1 1 1V20a1 1 0 0 1-1 1A17 17 0 0 1 3 4a1 1 0 0 1 1-1h3.5a1 1 0 0 1 1 1c0 1.25.2 2.45.57 3.57a1 1 0 0 1-.25 1z"/></svg>+1 (800) 555.0142</li>
        <li><svg viewBox="0 0 24 24"><path d="M6.6 10.8a15 15 0 0 0 6.6 6.6l2.2-2.2a1 1 0 0 1 1-.25 11.4 11.4 0 0 0 3.6.57 1 1 0 0 1 1 1V20a1 1 0 0 1-1 1A17 17 0 0 1 3 4a1 1 0 0 1 1-1h3.5a1 1 0 0 1 1 1c0 1.25.2 2.45.57 3.57a1 1 0 0 1-.25 1z"/></svg>+1 (800) 555.0187</li>
        <li><svg viewBox="0 0 24 24"><circle cx="12" cy="12" r="9" fill="none" stroke="#fff" stroke-width="2"/><path d="M3 12h18M12 3c3 3 3 15 0 18M12 3c-3 3-3 15 0 18" fill="none" stroke="#fff" stroke-width="1.6"/></svg>www.veltrapro.com</li>
        <li><svg viewBox="0 0 24 24"><path d="M2 5h20v14H2z" fill="none" stroke="#fff" stroke-width="2"/><path d="M2 5l10 8 10-8" fill="none" stroke="#fff" stroke-width="2"/></svg>info@veltrapro.com</li>
      </ul>
    </div>
  </div>
  <div class="mail-side"></div>
</section>

<section class="postcard postcard--front">
  <div class="hero-photo" role="img" aria-label="Photo of a smiling consultant in a bright office"></div>
  <h1 class="headline">Your Global<br>Small Business<br>Consulting Team</h1>
  <p class="intro-box">We will provide your company individualized business solutions and strategies, paired with dependable partners across every market you enter. Our team turns fresh ideas into practical plans so your venture grows with confidence.</p>
  <div class="logo-box front-logo"><span class="mark"></span>Veltra Pro</div>
  <div class="about">
    <h2>Who We Are</h2>
    <p>Consultants here at Veltra Pro come from an impressive range of backgrounds and experience in the global market. Their diversity lets us find the best solution for making your ideas successful, wherever your business is headed.</p>
    <h2>Our Mission Statement</h2>
    <p>“Veltra Pro is an international small business consulting firm that contributes to the success of our domestic and global clients by providing business processes and market-specific consulting services.”</p>
  </div>
  <div class="front-footer">
    <span><svg viewBox="0 0 24 24"><path d="M6.6 10.8a15 15 0 0 0 6.6 6.6l2.2-2.2a1 1 0 0 1 1-.25 11.4 11.4 0 0 0 3.6.57 1 1 0 0 1 1 1V20a1 1 0 0 1-1 1A17 17 0 0 1 3 4a1 1 0 0 1 1-1h3.5a1 1 0 0 1 1 1c0 1.25.2 2.45.57 3.57a1 1 0 0 1-.25 1z"/></svg>+1 (800) 555.0187</span>
    <span><svg viewBox="0 0 24 24"><path d="M6.6 10.8a15 15 0 0 0 6.6 6.6l2.2-2.2a1 1 0 0 1 1-.25 11.4 11.4 0 0 0 3.6.57 1 1 0 0 1 1 1V20a1 1 0 0 1-1 1A17 17 0 0 1 3 4a1 1 0 0 1 1-1h3.5a1 1 0 0 1 1 1c0 1.25.2 2.45.57 3.57a1 1 0 0 1-.25 1z"/></svg>+1 (800) 555.0142</span>
    <span><svg viewBox="0 0 24 24"><path d="M2 5h20v14H2z" fill="none" stroke="#fff" stroke-width="2"/><path d="M2 5l10 8 10-8" fill="none" stroke="#fff" stroke-width="2"/></svg>info@veltrapro.com</span>
    <span><svg viewBox="0 0 24 24"><circle cx="12" cy="12" r="9" fill="none" stroke="#fff" stroke-width="2"/><path d="M3 12h18M12 3c3 3 3 15 0 18M12 3c-3 3-3 15 0 18" fill="none" stroke="#fff" stroke-width="1.6"/></svg>www.veltrapro.com</span>
  </div>
</section>

</body>
</html>
```